Advertisement Coaching practice

I need an advertisement (to be printed in newspaper). I have a coaching practice where I offer coaching, workshops family constellations and relationship therapy. The ad needs to express calmness, inspiration to transform but also not dull and boring. It would be great if you could use the colors from my logo into the ad.

Dimensions are: 13,04 cm Width x 9,72 cm Height.

I will add my previous self-made ad, my company logo, a portrait photo of myself and the text I want to add. Also my contact details should be visible as well.

Requirements
Nice to have
• I have updated the brief with a flyer that I had previously made by a designer. It would be a nice to have if the ad ties in with that. You can also look at my website at www.fernbrook.nu to see what colors I used there.

```html
<!DOCTYPE html>
<html lang="nl">
<head>
<meta charset="utf-8">
<title>Advertentie coachingpraktijk</title>
<link rel="stylesheet" href="https://fonts.googleapis.com/css2?family=Montserrat:wght@800&family=Quicksand:wght@500;600&display=swap">
<style>
  :root {
    --navy: #1d3a5f;
    --navy-deep: #15304f;
    --gold-text: #d6b25b;
    --gold-band: #a98a3b;
    --white: #ffffff;
    --ink: #2b2b2b;
    --grey: #5a5a5a;
    --backdrop: #c8c8c8;
  }
  html, body {
    margin: 0; padding: 0;
    width: 1200px; height: 720px;
    overflow: hidden;
    background: var(--backdrop);
  }
  .ad {
    position: absolute;
    left: 117px; top: 0;
    width: 966px; height: 720px;
    background: var(--white);
    overflow: hidden;
    font-family: "Quicksand", sans-serif;
  }
  .ad-shapes { position: absolute; inset: 0; }
  .headline {
    position: absolute;
    right: 41px; top: 38px;
    margin: 0;
    text-align: right;
    font-family: "Montserrat", sans-serif;
    font-weight: 800;
    font-size: 44px;
    line-height: 52px;
    color: var(--gold-text);
  }
  .intro {
    position: absolute;
    right: 41px; top: 198px;
    width: 580px;
    margin: 0;
    text-align: right;
    font-weight: 500;
    font-size: 21.5px;
    line-height: 26px;
    color: var(--white);
  }
  .intro-pill {
    position: absolute;
    left: 616px; top: 358px;
    width: 350px; height: 61px;
    background: var(--navy);
    border-radius: 30px 0 0 30px;
  }
  .intro-pill p {
    margin: 0;
    position: absolute; right: 41px; top: 6px;
    text-align: right;
    font-weight: 500;
    font-size: 21px;
    line-height: 26px;
    color: var(--gold-text);
    white-space: nowrap;
  }
  .intro-pill strong { color: var(--white); font-weight: 600; }
  .benefit {
    position: absolute;
    top: 515px;
    width: 160px;
    margin: 0;
    text-align: center;
    font-weight: 500;
    font-size: 13px;
    line-height: 15.5px;
    color: var(--ink);
  }
  .benefit--patterns { left: 464px; }
  .benefit--conflicts { left: 624px; }
  .benefit--connection { left: 772px; }
  .offer {
    position: absolute;
    right: 41px; top: 581px;
    width: 620px;
    margin: 0;
    text-align: right;
    font-weight: 500;
    font-size: 12.3px;
    line-height: 16px;
    color: var(--grey);
  }
  .contact-bar {
    position: absolute;
    left: 308px; top: 655px;
    width: 658px; height: 25px;
    background: var(--navy);
    color: var(--white);
    font-weight: 500;
    font-size: 15.5px;
    line-height: 25px;
    white-space: nowrap;
    padding-left: 8px;
    box-sizing: border-box;
  }
  .brand {
    position: absolute;
    left: 57px; top: 540px;
    width: 200px;
    text-align: center;
  }
  .brand-dot {
    display: block;
    width: 62px; height: 62px;
    margin: 0 auto 8px;
    border: 2px solid var(--grey);
    border-radius: 50%;
    box-sizing: border-box;
  }
  .brand-name {
    font-family: "Quicksand", sans-serif;
    font-weight: 500;
    font-size: 40px;
    line-height: 44px;
    color: var(--grey);
  }
</style>
</head>
<body>
<div class="ad">
  <svg class="ad-shapes" width="966" height="720" viewBox="0 0 966 720">
    <defs>
      <linearGradient id="navyTexture" x1="0" y1="0" x2="1" y2="1">
        <stop offset="0" stop-color="#1a3658"/>
        <stop offset="0.5" stop-color="#234468"/>
        <stop offset="1" stop-color="#1a3658"/>
      </linearGradient>
      <linearGradient id="portraitTone" x1="0" y1="0" x2="0" y2="1">
        <stop offset="0" stop-color="#3b4252"/>
        <stop offset="0.45" stop-color="#a9795c"/>
        <stop offset="1" stop-color="#bcc8d8"/>
      </linearGradient>
    </defs>
    <rect class="navy-field" width="966" height="720" fill="url(#navyTexture)"/>
    <rect class="portrait" x="30" y="20" width="430" height="560" rx="8" fill="url(#portraitTone)" role="img" aria-label="Portretfoto van de coach"/>
    <path class="gold-wave" fill="var(--gold-band)"
      d="M0,480 C100,560 200,500 300,450 C420,395 560,310 640,288 C720,268 800,328 880,333 C930,335 955,310 966,282 L966,720 L0,720 Z"/>
    <path class="white-field" fill="var(--white)"
      d="M0,505 C110,580 220,525 320,478 C440,425 570,350 650,324 C730,302 800,350 880,352 C930,352 955,328 966,304 L966,720 L0,720 Z"/>

    <g class="benefit-icon" fill="none" stroke="var(--gold-band)" stroke-width="2.5">
      <circle cx="544" cy="474" r="34"/>
      <circle cx="704" cy="474" r="34"/>
      <circle cx="852" cy="474" r="34"/>
    </g>
    <!-- patterns: open hand holding a sphere -->
    <g fill="var(--gold-band)">
      <circle cx="550" cy="463" r="12"/>
      <path d="M524,484 h6 v10 h-6 z M532,485 c8,-2 14,0 20,3 l10,-4 c3,-1 5,3 2,5 l-14,7 h-18 z"/>
    </g>
    <g fill="none" stroke="var(--white)" stroke-width="1.2">
      <ellipse cx="550" cy="463" rx="9" ry="3.5"/>
      <ellipse cx="550" cy="463" rx="9" ry="3.5" transform="rotate(60 550 463)"/>
      <ellipse cx="550" cy="463" rx="9" ry="3.5" transform="rotate(-60 550 463)"/>
    </g>
    <!-- conflicts: two hands meeting -->
    <g fill="var(--gold-band)">
      <path d="M681,462 l12,-8 l14,6 l-12,10 z"/>
      <path d="M727,462 l-12,-8 l-16,10 l6,4 z"/>
      <path d="M689,468 l14,-4 l18,2 l-6,16 c-3,3 -8,3 -11,0 l-15,-10 z"/>
    </g>
    <!-- connection: network around a plus -->
    <g stroke="var(--gold-band)" stroke-width="1.5" fill="none">
      <polygon points="852,452 871,463 871,485 852,496 833,485 833,463"/>
      <line x1="852" y1="452" x2="852" y2="496"/>
      <line x1="833" y1="463" x2="871" y2="485"/>
      <line x1="871" y1="463" x2="833" y2="485"/>
    </g>
    <g fill="var(--gold-band)">
      <circle cx="852" cy="452" r="3"/><circle cx="871" cy="463" r="3"/><circle cx="871" cy="485" r="3"/>
      <circle cx="852" cy="496" r="3"/><circle cx="833" cy="485" r="3"/><circle cx="833" cy="463" r="3"/>
      <circle cx="852" cy="474" r="9"/>
    </g>
    <path d="M848,474 h8 M852,470 v8" stroke="var(--white)" stroke-width="2.5"/>
  </svg>

  <h1 class="headline">COACHING,<br>FAMILIEOPSTELLINGEN<br>&amp; RELATIETHERAPIE</h1>
  <p class="intro">Trauma’s en negatieve ervaringen vormen ons en blijven nog lang voelbaar. Ze kunnen groei of geluk in de weg staan.</p>

  <div class="intro-pill">
    <p>IK BEN <strong>AMARA</strong> EN<br>ONDERSTEUN JE BIJ HET:</p>
  </div>

  <p class="benefit benefit--patterns">Doorbreken van belemmerende patronen</p>
  <p class="benefit benefit--conflicts">Beter omgaan met conflicten</p>
  <p class="benefit benefit--connection">In gezonde verbinding met elkaar als koppel of met anderen komen</p>

  <p class="offer">Maandelijks geef ik workshops familieopstellingen. Ook houd ik themasessies rond adoptie, moeder-dochterdynamiek of relaties. Ook bied ik individuele coaching, relatietherapie en retraites aan. Kijk op de website voor meer info of neem contact open ontdek wat het beste bij jou past.</p>

  <div class="contact-bar">Amara Vos &nbsp;&nbsp;&nbsp;| M: info@fernbrook.nu &nbsp;&nbsp;| T: 06-12 34 56 78 | &nbsp;&nbsp;&nbsp;www.fernbrook.nu</div>

  <div class="brand">
    <span class="brand-dot"></span>
    <div class="brand-name">fernbrook</div>
  </div>
</div>
</body>
</html>
```